BrivoMatex. Lantern for the Steady Growth. Business card

Professional business card for BrivoMatex (Lantern for the Steady Growth)
My rationale: Strategy-> Execution-> Results-> Value that lead to the BrivoMatex name: We put the Lantern for the Steady Growth.
We deliver value to our customers helping them at defining a good strategy (cyan arrow). 90% of well formulated strategies fail due to poor execution so we also consider strategical execution very important (green arrow). Due to the execution we obtain the results (blue arrow). Finally, the results provide feedback to redefine strategy, and the new strategy has to be executed and new results obtained providing new feedback and on and on. It's like a wheel that finally, must create corporate value: value for shareholders, staholders, employees, providers...-

Target Market(s)

CEOs and steering comitees , invewrnent funds

Industry/Entity Type

Business Consultant

Contact Information for Business Card

Tommaso Ferlini
CEO & Founder
tommaso.ferlini@brivomatex.example
Mobile: +34 611.205.938
www.brivomatex.example

Colors

Designer to choose colors to be used in the design.

Requirements
Nice to have
• Nice to hace the words: Strategy, execution, results
• Nice to vave the claim: Lantern for the Steady Growth
• The three colors should be shown:
• cyan for STRATEGY
• green for EXECUTION
• blue for RESULTS
Should not have
• Complete black background

```html
<!DOCTYPE html>
<html lang="en">
<head>
<meta charset="utf-8">
<title>BrivoMatex Business Card</title>
<link href="https://fonts.googleapis.com/css2?family=Open+Sans:wght@400;600;700;800&display=swap" rel="stylesheet">
<style>
  :root {
    --navy: #233f95;
    --green: #96c83a;
    --cyan: #2aabe2;
    --paper: #ffffff;
    --backdrop: #e9eaec;
    --rule: #8f96b8;
  }
  html, body {
    margin: 0;
    padding: 0;
    width: 1200px;
    height: 880px;
    overflow: hidden;
    background: var(--backdrop);
    font-family: "Open Sans", Arial, sans-serif;
  }
  .sheet {
    position: relative;
    width: 1200px;
    height: 880px;
  }
  .card {
    position: absolute;
    left: 260px;
    width: 680px;
    height: 390px;
    background: var(--paper);
    border-radius: 18px;
    overflow: hidden;
    box-shadow: 0 6px 18px rgba(20, 30, 60, 0.18);
  }
  .card--front { top: 35px; }
  .card--back { top: 465px; }

  /* Front */
  .front-brand {
    position: absolute;
    left: 0;
    right: 0;
    top: 150px;
    text-align: center;
    color: var(--navy);
    font-weight: 800;
    font-size: 62px;
    letter-spacing: -1px;
    line-height: 1;
  }
  .front-brand .brand-dot {
    display: inline-block;
    width: 22px;
    height: 22px;
    border-radius: 50%;
    background: var(--navy);
    margin-right: 14px;
    vertical-align: middle;
    position: relative;
    top: -6px;
  }
  .front-domain {
    position: absolute;
    left: 0;
    right: 0;
    top: 228px;
    text-align: center;
    color: var(--navy);
    font-weight: 700;
    font-size: 17px;
  }
  .front-url {
    position: absolute;
    left: 0;
    right: 0;
    bottom: 42px;
    text-align: center;
    color: var(--navy);
    font-weight: 700;
    font-size: 15px;
  }

  /* Back */
  .base-band {
    position: absolute;
    left: 0;
    right: 0;
    bottom: 0;
    height: 44px;
    background: var(--navy);
  }
  .base-rule {
    position: absolute;
    left: 0;
    right: 0;
    bottom: 52px;
    height: 4px;
    background: var(--green);
  }
  .back-brand {
    position: absolute;
    left: 40px;
    top: 128px;
    color: var(--navy);
    font-weight: 800;
    font-size: 44px;
    letter-spacing: -1px;
    line-height: 1;
  }
  .divider {
    position: absolute;
    left: 330px;
    top: 78px;
    width: 1px;
    height: 150px;
    background: var(--rule);
  }
  .contact {
    position: absolute;
    left: 352px;
    top: 78px;
  }
  .contact__name {
    margin: 0;
    color: var(--navy);
    font-weight: 800;
    font-size: 24px;
    line-height: 1.1;
  }
  .contact__role {
    margin: 2px 0 12px;
    color: var(--green);
    font-weight: 600;
    font-size: 14px;
  }
  .contact__list {
    list-style: none;
    margin: 0;
    padding: 0;
  }
  .contact__item {
    display: flex;
    align-items: center;
    gap: 9px;
    color: var(--navy);
    font-size: 15px;
    line-height: 1.55;
  }
  .contact__icon {
    width: 14px;
    height: 14px;
    flex: none;
  }
</style>
</head>
<body>
<main class="sheet">

  <section class="card card--front" aria-label="Card front">
    <div class="front-brand"><span class="brand-dot"></span>BrivoMatex</div>
    <div class="front-domain">brivomatex.example</div>
    <div class="front-url">www.brivomatex.example</div>
  </section>

  <section class="card card--back" aria-label="Card back">
    <div class="back-brand">BrivoMatex</div>
    <div class="divider"></div>

    <div class="contact">
      <h1 class="contact__name">Tommaso Ferlini</h1>
      <p class="contact__role">CEO &amp; Founder</p>
      <ul class="contact__list">
        <li class="contact__item">
          <svg class="contact__icon" viewBox="0 0 16 16" aria-hidden="true">
            <path d="M3.5 1.5 L6 1.5 L7 5 L5.3 6.3 C6.2 8.2 7.8 9.8 9.7 10.7 L11 9 L14.5 10 L14.5 12.5 C14.5 13.6 13.6 14.5 12.5 14.5 C6.9 14.5 1.5 9.1 1.5 3.5 C1.5 2.4 2.4 1.5 3.5 1.5 Z" fill="var(--green)"/>
          </svg>
          +34 611.205.938
        </li>
        <li class="contact__item">
          <svg class="contact__icon" viewBox="0 0 16 16" aria-hidden="true">
            <rect x="1" y="3" width="14" height="10" rx="1" fill="var(--green)"/>
            <path d="M1.5 3.8 L8 9 L14.5 3.8" fill="none" stroke="#fff" stroke-width="1.3"/>
          </svg>
          tommaso.ferlini@brivomatex.example
        </li>
        <li class="contact__item">
          <svg class="contact__icon" viewBox="0 0 16 16" aria-hidden="true">
            <circle cx="8" cy="8" r="6.5" fill="none" stroke="var(--green)" stroke-width="1.4"/>
            <ellipse cx="8" cy="8" rx="2.8" ry="6.5" fill="none" stroke="var(--green)" stroke-width="1.2"/>
            <path d="M1.5 8 H14.5 M2.5 5 H13.5 M2.5 11 H13.5" stroke="var(--green)" stroke-width="1.1"/>
          </svg>
          www.brivomatex.example
        </li>
      </ul>
    </div>

    <div class="base-rule"></div>
    <div class="base-band"></div>
  </section>

</main>
</body>
</html>
```